Insurance company needs a business card design

We need a business card design for a Massachusetts-based insurance company Veloria Insurance, LLC. We provide auto insurance to Hispanic (Spanish- or Portuguese-speaking) immigrants in the United States. We will give these business cards to auto dealers where such customers typically go to purchase vehicles. We will provide a solution to the dealers to provide easy insurance to the customers buying cars at their dealerships. Veloria is the Spanish word for protection.
Contact Information for Business Card
Name, Designation, Company Name, Address, Phone Number, Email, Website
Look and feel
Each slider illustrates characteristics of the customer's brand and the style your logo design should communicate.

```html
<!DOCTYPE html>
<html lang="en">
<head>
<meta charset="utf-8">
<title>Veloria Insurance — Business Card</title>
<link rel="stylesheet" href="https://fonts.googleapis.com/css2?family=Montserrat:wght@700&family=Nunito+Sans:wght@400&display=swap">
<style>
  :root {
    --navy: #063f75;
    --orange: #ec7f0c;
    --paper: #ffffff;
    --backdrop: #e9ebef;
    --ink: #0c3a66;
  }
  * { box-sizing: border-box; margin: 0; padding: 0; }
  html, body { width: 1199px; height: 1200px; overflow: hidden; }
  body {
    background: var(--backdrop);
    display: flex;
    flex-direction: column;
    align-items: center;
    justify-content: center;
    gap: 60px;
  }
  .card {
    width: 840px;
    height: 480px;
    border-radius: 6px;
    box-shadow: 0 10px 28px rgba(10, 30, 60, 0.18);
    position: relative;
    overflow: hidden;
  }
  .card--front {
    background: var(--paper);
    padding: 110px 0 0 150px;
  }
  .holder-name {
    font-family: "Montserrat", sans-serif;
    font-weight: 700;
    font-size: 40px;
    letter-spacing: 1.5px;
    color: var(--navy);
  }
  .holder-title {
    font-family: "Nunito Sans", sans-serif;
    font-size: 26px;
    letter-spacing: 0.5px;
    color: var(--orange);
    margin-top: 6px;
  }
  .divider {
    width: 205px;
    height: 3px;
    background: var(--orange);
    margin: 28px 0 40px;
  }
  .contact-list {
    list-style: none;
    font-family: "Nunito Sans", sans-serif;
    font-size: 26px;
    line-height: 1.45;
    color: var(--ink);
    letter-spacing: 0.5px;
  }
  .contact-list .label {
    display: inline-block;
    width: 48px;
  }
  .card--back {
    background: var(--navy);
    display: flex;
    align-items: center;
    justify-content: center;
    gap: 26px;
  }
  .brand-mark {
    width: 34px;
    height: 34px;
    background: var(--orange);
  }
  .brand-name {
    font-family: "Montserrat", sans-serif;
    font-weight: 700;
    font-size: 58px;
    letter-spacing: 3px;
    color: var(--paper);
    text-transform: uppercase;
  }
</style>
</head>
<body>
  <section class="card card--front" aria-label="Business card front">
    <h1 class="holder-name">MATEO RIVERA</h1>
    <p class="holder-title">General manager</p>
    <div class="divider"></div>
    <ul class="contact-list">
      <li><span class="label">T:</span>(866) 555-0182</li>
      <li><span class="label">M:</span>info@veloriainsurance.com</li>
      <li><span class="label">W:</span>veloriainsurance.com</li>
    </ul>
  </section>

  <section class="card card--back" aria-label="Business card back">
    <div class="brand-mark"></div>
    <p class="brand-name">Veloria Insurance</p>
  </section>
</body>
</html>
```